Wholesale in Gold Jewellery & Gold Bullion

We are an established gold jewellery and gold bullion wholesaler selling these products to international clients. We already have a name and logo of our company, hence please view attached current card design. We need a completely new design to compliment our business and industry and the final design should be new and elegant.

Contact Information for Business Card

New card details must be same as per current card. Like logo, name, tel no. & etc.

Colors

Designer to choose colors to be used in the design.

```html
<!DOCTYPE html>
<html lang="en">
<head>
<meta charset="utf-8">
<title>Arundel &amp; Co Business Card</title>
<link rel="stylesheet" href="https://fonts.googleapis.com/css2?family=Montserrat:wght@400;500;600&display=swap">
<style>
  :root {
    --backdrop: #5a3f27;
    --card: #fbfbfa;
    --gold: #e0b33a;
    --ink-dark: #3a2a22;
    --ink-grey: #5c5c5c;
    --ink-light: #8a8a8a;
  }
  * { margin: 0; padding: 0; box-sizing: border-box; }
  html, body {
    width: 1200px; height: 894px; overflow: hidden;
    background: var(--backdrop);
  }
  .stage {
    width: 1200px; height: 894px;
    display: flex; align-items: center; justify-content: center;
  }
  .card {
    position: relative;
    width: 470px; height: 780px;
    background: var(--card);
    font-family: "Montserrat", sans-serif;
    text-align: center;
    box-shadow: 0 10px 30px rgba(0,0,0,0.35);
  }
  .brand {
    position: absolute; top: 120px; left: 0; right: 0;
    display: flex; flex-direction: column; align-items: center;
  }
  .brand-dot {
    width: 84px; height: 84px; border-radius: 50%;
    background: var(--gold);
  }
  .brand-name {
    margin-top: 26px;
    font-weight: 600; font-size: 24px; letter-spacing: 0.5px;
    color: var(--ink-dark);
  }
  .person {
    position: absolute; top: 330px; left: 0; right: 0;
  }
  .person-name {
    font-weight: 500; font-size: 30px; color: var(--gold);
  }
  .person-title {
    margin-top: 2px;
    font-weight: 400; font-size: 22px; color: var(--ink-light);
  }
  .contact-icons {
    position: absolute; top: 470px; left: 0; right: 0;
    display: flex; justify-content: center; gap: 22px;
  }
  .contact-icons svg { width: 20px; height: 20px; }
  .contact-lines {
    position: absolute; top: 525px; left: 0; right: 0;
    list-style: none;
    font-size: 18px; line-height: 30px; color: var(--ink-grey);
  }
  .address {
    position: absolute; bottom: 48px; left: 0; right: 0;
    font-size: 19px; color: var(--ink-grey);
  }
</style>
</head>
<body>
<main class="stage">
  <article class="card">
    <header class="brand">
      <span class="brand-dot"></span>
      <h1 class="brand-name">ARUNDEL &amp; CO PTE LTD</h1>
    </header>

    <section class="person">
      <h2 class="person-name">Rohan Verapathi</h2>
      <p class="person-title">Director</p>
    </section>

    <div class="contact-icons" aria-hidden="true">
      <svg viewBox="0 0 20 20" fill="none" stroke="var(--gold)" stroke-width="1.6">
        <rect x="5.5" y="2" width="9" height="16" rx="1.5"/>
        <line x1="9" y1="15.5" x2="11" y2="15.5"/>
      </svg>
      <svg viewBox="0 0 20 20" fill="var(--gold)">
        <path d="M6 2c1 0 2 3 2 4s-1.5 1.5-1.5 2.5 3 5 4 5S12 12 13 12s4 1 4 2-2 4-3.5 4C8 18 2 10 2 6 2 4 5 2 6 2z"/>
      </svg>
      <svg viewBox="0 0 20 20" fill="none" stroke="var(--gold)" stroke-width="1.6">
        <rect x="6" y="2" width="8" height="6"/>
        <rect x="2.5" y="8" width="15" height="7" rx="1"/>
        <rect x="6" y="13" width="8" height="5" fill="var(--card)"/>
      </svg>
      <svg viewBox="0 0 20 20" fill="var(--gold)">
        <rect x="2" y="5" width="16" height="11" rx="1"/>
        <path d="M2.5 5.5 10 11l7.5-5.5" fill="none" stroke="var(--card)" stroke-width="1.4"/>
      </svg>
    </div>

    <ul class="contact-lines">
      <li class="contact-mobile">+65 9100 2345</li>
      <li class="contact-phone">+65 6100 4400</li>
      <li class="contact-fax">+65 6100 4401</li>
      <li class="contact-email">rohan@arundelco.com</li>
    </ul>

    <p class="address">12 Lorong Teak, Singapore 100001</p>
  </article>
</main>
</body>
</html>
```